Book Cover

Hello!
I need someone to design a book cover with the title, subtitle and one of the photos attached.

- Title: Beyond the Grey Hours - By Corwin Ashdale
- Subtitle: A Steady Handbook for finding calm and strength after hard news.

```html
<!DOCTYPE html>
<html lang="en">
<head>
<meta charset="utf-8">
<title>Beyond the Grey Hours — Corwin Ashdale</title>
<link rel="stylesheet" href="https://fonts.googleapis.com/css2?family=Barlow+Condensed:wght@600;800&family=Montserrat:wght@600&display=swap">
<style>
  :root {
    --cover: #e8eaee;
    --ink: #1e1e1f;
    --band: #2a2a2b;
    --gold: #e5a837;
    --gold-deep: #b98422;
    --white: #ffffff;
    --sky: #b9cde2;
    --sky-deep: #6f8fb4;
    --frame: #2b2b2b;
  }
  * { margin: 0; padding: 0; box-sizing: border-box; }
  html, body { width: 978px; height: 1200px; overflow: hidden; }
  body { background: var(--cover); }
  .cover {
    position: relative;
    width: 978px;
    height: 1200px;
    background: var(--cover);
    overflow: hidden;
  }
  .title-accent {
    position: absolute;
    left: 0; top: 0;
  }
  .title {
    position: absolute;
    top: 30px;
    left: 0;
    width: 978px;
    text-align: center;
    font-family: "Barlow Condensed", sans-serif;
    font-weight: 800;
    font-size: 132px;
    line-height: 0.72;
    letter-spacing: -1px;
    color: var(--ink);
    text-transform: uppercase;
  }
  .title span { display: block; padding-top: 20px; }
  .subtitle-band {
    position: absolute;
    left: 0;
    top: 264px;
    width: 874px;
    height: 85px;
    background: var(--band);
    padding: 9px 0 0 174px;
    font-family: "Barlow Condensed", sans-serif;
    font-weight: 600;
    font-size: 34px;
    line-height: 34px;
    color: var(--white);
    text-transform: uppercase;
  }
  .subtitle-band .highlight { color: var(--gold); }
  .author {
    position: absolute;
    top: 362px;
    left: 0;
    width: 1008px;
    text-align: center;
    font-family: "Montserrat", sans-serif;
    font-weight: 600;
    font-size: 19px;
    letter-spacing: 5px;
    color: var(--ink);
    text-transform: uppercase;
  }
  .portrait-art {
    position: absolute;
    left: 0;
    top: 430px;
  }
</style>
</head>
<body>
  <main class="cover">
    <svg class="title-accent" width="978" height="260" viewBox="0 0 978 260" aria-hidden="true">
      <defs>
        <linearGradient id="goldSheen" x1="0" y1="0" x2="1" y2="1">
          <stop offset="0" stop-color="var(--gold-deep)"/>
          <stop offset="0.5" stop-color="var(--gold)"/>
          <stop offset="1" stop-color="var(--gold-deep)"/>
        </linearGradient>
      </defs>
      <polygon points="520,40 790,48 850,240 200,248 330,130" fill="url(#goldSheen)" opacity="0.9"/>
    </svg>

    <h1 class="title"><span>Beyond the</span><span>Grey Hours</span></h1>

    <p class="subtitle-band">A Steady Handbook for finding calm<br>and <span class="highlight">strength</span> after hard news.</p>

    <p class="author">By Corwin Ashdale</p>

    <svg class="portrait-art" width="978" height="770" viewBox="0 0 978 770">
      <defs>
        <linearGradient id="photoTone" x1="0" y1="0" x2="1" y2="1">
          <stop offset="0" stop-color="#6b5a46"/>
          <stop offset="0.35" stop-color="var(--sky)"/>
          <stop offset="0.7" stop-color="var(--sky-deep)"/>
          <stop offset="1" stop-color="#2c3f86"/>
        </linearGradient>
      </defs>
      <rect x="200" y="120" width="620" height="560" fill="none" stroke="#9a9a9a" stroke-width="1.5" transform="rotate(-6 510 400)"/>
      <rect x="180" y="80" width="640" height="610" fill="none" stroke="var(--frame)" stroke-width="2.5" transform="rotate(-9 500 385)"/>
      <rect x="180" y="19" width="99" height="188" fill="var(--gold)"/>
      <rect x="750" y="420" width="188" height="287" fill="var(--gold)"/>
      <path role="img" aria-label="Photo of an older man with grey hair and beard in a blue jacket, looking upward outdoors"
        d="M120,150 L300,60 L380,20 L520,40 L680,30 L800,70 L880,130 L930,240 L900,330 L950,420 L930,520 L880,600 L790,660 L650,640 L520,700 L400,690 L250,640 L140,600 L60,520 L90,430 L40,340 L80,250 Z"
        fill="url(#photoTone)"/>
      <rect x="204" y="436" width="99" height="82" fill="var(--band)"/>
    </svg>
  </main>
</body>
</html>
```